We currently have a good logo and we want business cards that can display our logo but also represent our industry - telecom construction - We are a construction company specializing in telecom construction such as installation of fiber optic cable throughout cities and across the country. Nationwide services
We are large enough to handle most any project yet small enough to be a flexible partner and resource.

Target Market(s)

U.S. based telecom carriers and providers

Industry/Entity Type

Construction

Contact Information for Business Card

Business cards should include our logo, phone number and website address. Also, including some information as to our core services would be good.

Colors

Designer to choose colors to be used in the design.

Requirements
Must have
• Colors based on logo
• Must use our logo
• Logo, name, email, website address, phone number
• Tovasco Conduit
• Brent Halvik
• Director of Business Development
• (555) 271-0386
• www.TVSQ-example.com
Nice to have
• Construction services including:
• Small Cell Construction
• Boring/Drilling
• Plowing / Trenching
• Conduit installation
• Fiber pulling
• splicing
• building entries
• Aerial construction
• Aerial Make Ready
• Make Ready Engineering
Should not have
• We are open to ideas

```html
<!DOCTYPE html>
<html lang="en">
<head>
<meta charset="UTF-8">
<title>Tovasco Conduit – Business Card</title>
<link href="https://fonts.googleapis.com/css2?family=Montserrat:wght@400;500;700;800&family=Roboto+Condensed:wght@400;500&family=Rubik:wght@400;500&display=swap" rel="stylesheet">
<style>
  :root {
    --bg: #1f1f1f;
    --blue-deep: #1560b8;
    --blue-mid: #1a86d4;
    --blue-light: #22aee6;
    --navy: #0d4fa8;
    --grey: #8c8c8c;
    --grey-light: #c9c9c9;
    --ink: #3c3c3c;
    --accent: #b5672f;
    --white: #ffffff;
  }
  * { box-sizing: border-box; margin: 0; padding: 0; }
  html, body { width: 1200px; height: 900px; overflow: hidden; }
  body {
    background: var(--bg);
    position: relative;
    font-family: "Montserrat", sans-serif;
  }
  .card {
    position: absolute;
    left: 240px;
    width: 720px;
    height: 400px;
    overflow: hidden;
    box-shadow: 0 10px 30px rgba(0,0,0,.55);
  }

  /* Back side */
  .card-back {
    top: 30px;
    background: linear-gradient(100deg, var(--blue-deep) 0%, var(--blue-mid) 40%, var(--blue-light) 62%, var(--blue-mid) 80%, var(--blue-deep) 100%);
    color: var(--white);
  }
  .card-back .brand-name {
    position: absolute;
    left: 70px;
    top: 160px;
    width: 300px;
    font-weight: 800;
    font-size: 36px;
    line-height: 1.1;
    text-transform: uppercase;
    color: var(--white);
  }
  .card-back .divider {
    position: absolute;
    left: 395px;
    top: 95px;
    width: 2px;
    height: 215px;
    background: var(--accent);
  }
  .services {
    position: absolute;
    left: 425px;
    top: 92px;
    font-family: "Rubik", sans-serif;
  }
  .services-heading {
    font-size: 15px;
    color: var(--accent);
    margin-bottom: 2px;
  }
  .services-list { list-style: none; }
  .services-list li {
    font-size: 16px;
    line-height: 19px;
    padding-left: 22px;
    position: relative;
  }
  .services-list li::before {
    content: "";
    position: absolute;
    left: 4px;
    top: 6px;
    width: 8px;
    height: 8px;
    border-radius: 50%;
    background: var(--white);
  }

  /* Front side */
  .card-front {
    top: 470px;
    background: var(--white);
  }
  .card-front .brand-name {
    position: absolute;
    left: 60px;
    top: 45px;
    width: 300px;
    font-weight: 800;
    font-size: 34px;
    line-height: 1.1;
    text-transform: uppercase;
    color: var(--navy);
  }
  .person-name {
    position: absolute;
    left: 60px;
    top: 165px;
    font-weight: 800;
    font-size: 30px;
    color: var(--navy);
    letter-spacing: .5px;
  }
  .person-title {
    position: absolute;
    left: 60px;
    top: 204px;
    font-family: "Roboto Condensed", sans-serif;
    font-size: 20px;
    color: var(--ink);
  }
  .title-rule {
    position: absolute;
    left: 60px;
    top: 243px;
    width: 280px;
    height: 4px;
    background: linear-gradient(90deg, var(--grey-light), var(--blue-light) 40%, var(--navy));
  }
  .contacts {
    position: absolute;
    left: 60px;
    top: 266px;
    list-style: none;
  }
  .contacts li {
    display: flex;
    align-items: center;
    gap: 12px;
    font-size: 22px;
    color: var(--ink);
    line-height: 34px;
  }
  .contacts svg { width: 22px; height: 22px; flex: none; }
  .bands {
    position: absolute;
    right: 0;
    bottom: 0;
    width: 720px;
    height: 400px;
  }
</style>
</head>
<body>

  <section class="card card-back">
    <div class="brand-name">Tovasco Conduit</div>
    <div class="divider"></div>
    <div class="services">
      <p class="services-heading">Construction services including:</p>
      <ul class="services-list">
        <li>Small Cell Construction</li>
        <li>Boring/Drilling</li>
        <li>Plowing / Trenching</li>
        <li>Conduit installation</li>
        <li>Fiber pulling</li>
        <li>splicing</li>
        <li>building entries</li>
        <li>Aerial construction</li>
        <li>Aerial Make Ready</li>
        <li>Make Ready Engineering</li>
      </ul>
    </div>
  </section>

  <section class="card card-front">
    <div class="brand-name">Tovasco Conduit</div>
    <div class="person-name">BRENT HALVIK</div>
    <div class="person-title">Director of Business Development</div>
    <div class="title-rule"></div>
    <ul class="contacts">
      <li>
        <svg viewBox="0 0 24 24" fill="none" stroke="#1a86d4" stroke-width="1.8">
          <circle cx="12" cy="12" r="10"/>
          <path d="M8.5 7.5l2 2-1.2 1.5c.8 1.6 1.9 2.7 3.5 3.5l1.5-1.2 2 2-1.3 1.4c-3.5-.3-7.2-4-7.5-7.5z"/>
        </svg>
        (555) 271-0386
      </li>
      <li>
        <svg viewBox="0 0 24 24" fill="none" stroke="#1a86d4" stroke-width="1.8">
          <rect x="2" y="5" width="20" height="14" rx="1"/>
          <path d="M2 6l10 7 10-7"/>
        </svg>
        info@tvsq-example.com
      </li>
      <li>
        <svg viewBox="0 0 24 24" fill="none" stroke="#1a86d4" stroke-width="1.8">
          <circle cx="12" cy="12" r="10"/>
          <ellipse cx="12" cy="12" rx="4.5" ry="10"/>
          <path d="M2 12h20M4 7h16M4 17h16"/>
        </svg>
        www.TVSQ-example.com
      </li>
    </ul>
    <svg class="bands" viewBox="0 0 720 400" aria-hidden="true">
      <defs>
        <linearGradient id="bandBlue" x1="0" y1="1" x2="1" y2="0">
          <stop offset="0" stop-color="#22aee6"/>
          <stop offset="1" stop-color="#1560b8"/>
        </linearGradient>
        <linearGradient id="bandGrey" x1="0" y1="1" x2="1" y2="0">
          <stop offset="0" stop-color="#7a7a7a"/>
          <stop offset=".55" stop-color="#e6e6e6"/>
          <stop offset="1" stop-color="#6e6e6e"/>
        </linearGradient>
      </defs>
      <polygon points="330,400 720,150 720,400" fill="url(#bandBlue)"/>
      <polygon points="470,400 720,240 720,310 610,400" fill="url(#bandGrey)"/>
      <polygon points="610,400 720,310 720,400" fill="#22aee6"/>
    </svg>
  </section>

</body>
</html>
```